Industrial Professional Business Card Design (Vantrel Systems)

Would like professional looking business cards. Not too busy leaning towards minimal. Should have a slogan like:
"Industrial Automation and Control".

We are a tech company that programs industrial PLC computers. We also develop custom hardware solutions. Please use the logo for inspiration.

Target Market(s)

Mining, industrial, processing, automation, factory

Industry/Entity Type

Engineering

Contact Information for Business Card

Name, phone, email, website. job title.

Font styles to use
Other font styles liked:
• droid sans

Requirements
Must have
• Use colours that go well with the logo. Not too busy design.

```html
<!DOCTYPE html>
<html lang="en">
<head>
<meta charset="utf-8">
<title>Vantrel Systems – Business Card</title>
<link rel="stylesheet" href="https://fonts.googleapis.com/css2?family=Noto+Sans:wght@400;700&display=swap">
<style>
  :root {
    --backdrop: #e2e2e2;
    --navy: #1a4669;
    --orange: #e8641e;
    --card-white: #f4f4f4;
    --white: #ffffff;
  }
  * { margin: 0; padding: 0; box-sizing: border-box; }
  html, body {
    width: 1200px;
    height: 960px;
    overflow: hidden;
    background: var(--backdrop);
    font-family: "Noto Sans", "Droid Sans", Arial, sans-serif;
  }
  .stage { position: relative; width: 1200px; height: 960px; }

  .card {
    position: absolute;
    left: 322px;
    width: 559px;
    height: 342px;
  }
  .card--front { top: 117px; background: var(--navy); }
  .card--back  { top: 503px; background: var(--card-white); }

  /* Front */
  .front-brand {
    position: absolute;
    left: 0; right: 0;
    top: 92px;
    display: flex;
    flex-direction: column;
    align-items: center;
    gap: 22px;
  }
  .brand-dot {
    width: 88px; height: 88px;
    border-radius: 50%;
    background: var(--orange);
  }
  .front-brand .brand-name {
    color: var(--white);
    font-size: 36px;
    font-weight: 400;
    letter-spacing: -0.5px;
    line-height: 1;
  }

  /* Back */
  .back-brand {
    position: absolute;
    left: 40px;
    width: 220px;
    top: 108px;
    display: flex;
    flex-direction: column;
    align-items: center;
    gap: 16px;
  }
  .back-brand .brand-dot { width: 70px; height: 70px; }
  .back-brand .brand-name {
    color: var(--navy);
    font-size: 25px;
    font-weight: 400;
    letter-spacing: -0.3px;
    line-height: 1;
    white-space: nowrap;
  }
  .divider {
    position: absolute;
    left: 278px;
    top: 108px;
    width: 2px;
    height: 126px;
    background: var(--navy);
  }
  .person {
    position: absolute;
    left: 310px;
    top: 110px;
  }
  .person-name {
    color: var(--navy);
    font-size: 19px;
    font-weight: 700;
    line-height: 1.2;
  }
  .person-title {
    color: var(--orange);
    font-size: 14px;
    line-height: 1.4;
  }
  .contact-list {
    position: absolute;
    left: 310px;
    top: 174px;
    list-style: none;
  }
  .contact-item {
    display: flex;
    align-items: center;
    gap: 4px;
    color: var(--navy);
    font-size: 14px;
    line-height: 18.5px;
  }
  .contact-icon { width: 13px; height: 13px; flex: none; }
</style>
</head>
<body>
<main class="stage">

  <section class="card card--front" aria-label="Card front">
    <div class="front-brand">
      <span class="brand-dot" aria-hidden="true"></span>
      <span class="brand-name">Vantrel Systems</span>
    </div>
  </section>

  <section class="card card--back" aria-label="Card back">
    <div class="back-brand">
      <span class="brand-dot" aria-hidden="true"></span>
      <span class="brand-name">Vantrel Systems</span>
    </div>

    <div class="divider" aria-hidden="true"></div>

    <div class="person">
      <p class="person-name">Daniel Harper</p>
      <p class="person-title">President</p>
    </div>

    <ul class="contact-list">
      <li class="contact-item">
        <svg class="contact-icon" viewBox="0 0 16 16" aria-hidden="true">
          <path fill="#e8641e" d="M3.6 1.2l2.3 2.6c.4.4.3 1-.1 1.4L4.7 6.3c.8 1.9 2.9 4 4.9 4.9l1.1-1.1c.4-.4 1-.4 1.4-.1l2.6 2.3c.4.4.4 1 0 1.4l-1.3 1.3c-.7.7-1.8.8-2.7.4C6.3 13.6 2.4 9.7.6 5.2.2 4.3.4 3.2 1.1 2.5L2.2 1.2c.4-.4 1-.4 1.4 0z"/>
        </svg>
        <span>(123) 555-0147</span>
      </li>
      <li class="contact-item">
        <svg class="contact-icon" viewBox="0 0 16 16" aria-hidden="true">
          <rect x="1" y="3.5" width="14" height="9.5" fill="none" stroke="#e8641e" stroke-width="1.6"/>
          <path d="M1.5 4.2L8 9l6.5-4.8" fill="none" stroke="#e8641e" stroke-width="1.6"/>
        </svg>
        <span>daniel@vantrelsystems.com.au</span>
      </li>
      <li class="contact-item">
        <svg class="contact-icon" viewBox="0 0 16 16" aria-hidden="true">
          <g fill="none" stroke="#e8641e" stroke-width="1.3">
            <circle cx="8" cy="8" r="6.5"/>
            <ellipse cx="8" cy="8" rx="2.8" ry="6.5"/>
            <path d="M1.5 8h13M2.6 4.7h10.8M2.6 11.3h10.8"/>
          </g>
        </svg>
        <span>www.vantrelsystems.com.au</span>
      </li>
    </ul>
  </section>

</main>
</body>
</html>
```